Modern design for a Septic Tank maintenance company

Task Description
- The design should be based around the attached HPID (home page information design) called Tane Drain Septic Services HPID. The table boxes are just for approximate placement of information – you DON'T have to make it look exactly like this.
- Information only is in orange text. Copy to go on the design in black text. Some instructions are in the HPID. Please be creative! You don’t have to use the exact images provided if you have a better idea.

- The design needs to be clean and spacious. Please use the colours from the logos in the website design. LOTS of white too. Don't need to use all the images attached some are customer supplied and might only be good for the smaller images.

I've attached home page gallery example photo called Piha beach. You can use this or something similar - be creative please!

Width of content will be 1100 pixels when implemented as a web page. Header height (without nav bar) 150-160 pixels.

The winning PSD file will have to be provided as follows…
1. Canvas size of 2000px x 2000px - 72ppi in Adobe Photoshop (CS5 compatible)
2. Width of content section is 1100px wide - centered in the canvas
3. Any button rollovers/hovers in the PSD as hidden layers.
4. All fonts used must be Google fonts (except for the fonts in the header at the top of the page).
5. You will need to supply the chosen home page plus one example page (example page as a style guide for how all other pages will look). Example page is only the header and navigational bar at the top, an empty sector in the middle with a column (180 px wide) which can be left or right aligned which means the main sector is 920 pixels wide, and then the footer at the bottom of the page.

```html
<!DOCTYPE html>
<html lang="en">
<head>
<meta charset="utf-8">
<title>Tane Drain Septic Services</title>
<link href="https://fonts.googleapis.com/css2?family=Lato:ital,wght@0,400;0,700;0,900;1,400&family=Oswald:wght@500&family=Dancing+Script:wght@500&display=swap" rel="stylesheet">
<style>
:root{
  --teal:#1aa88a;
  --teal-dark:#0f8c72;
  --teal-deep:#0b6f5a;
  --orange:#ef8a0e;
  --ink:#2b2b2b;
  --muted:#8a8a8a;
  --card:#f4f4f4;
  --dark:#2e2e2e;
  --footer:#f6f6f6;
  --white:#fff;
}
*{box-sizing:border-box;margin:0;padding:0}
html,body{width:832px;height:1200px;overflow:hidden}
body{position:relative;background:var(--white);font-family:'Lato',sans-serif;color:var(--ink)}
.abs{position:absolute}

/* header */
.brand{left:90px;top:14px;display:flex;align-items:center;gap:10px}
.brand-dot{width:38px;height:38px;border-radius:50%;background:var(--teal)}
.brand-name{font:700 25px/1 'Lato',sans-serif;color:var(--teal-deep)}
.header-strap{left:92px;top:67px;width:230px;font:700 7px/9px 'Lato',sans-serif;color:#9a9a9a;text-transform:uppercase;letter-spacing:.1px}
.tagline{right:90px;top:4px;text-align:right;font:500 19px/28px 'Dancing Script',cursive;color:#333}
.phones{right:90px;top:65px;display:flex;align-items:center;gap:6px;font:400 15px/1 'Lato',sans-serif;color:#333}
.phones .or{color:var(--teal);font-weight:700;margin:0 6px}

/* nav */
.nav{left:0;top:95px;width:832px;height:30px;background:linear-gradient(#1fb395,#12987d);}
.nav ul{position:absolute;left:90px;top:0;display:flex;list-style:none;height:30px}
.nav li{font:700 10.5px/30px 'Lato',sans-serif;color:var(--white);padding:0 11px;border-right:1px solid rgba(255,255,255,.25)}
.nav li:last-child{border-right:0}
.nav li.active{background:var(--teal-deep)}

/* hero */
.hero{left:0;top:125px;width:832px;height:386px;background:linear-gradient(180deg,#6f8f55 0%,#4d6e3a 30%,#8ea98a 50%,#3f5b36 72%,#2a6f63 85%,#1f5b55 100%)}
.hero-title{left:0;top:280px;width:832px;text-align:center;font:500 29px/1 'Oswald',sans-serif;color:var(--white);text-transform:uppercase;text-shadow:0 1px 3px rgba(0,0,0,.5)}
.hero-sub{left:0;top:323px;width:832px;text-align:center;font:700 13px/1 'Lato',sans-serif;color:var(--white);text-shadow:0 1px 2px rgba(0,0,0,.5)}
.hero-btn{left:352px;top:357px;width:133px;height:28px;background:var(--teal);display:flex;align-items:center;justify-content:center;gap:6px;font:400 16px/1 'Lato',sans-serif;color:var(--white)}
.dots{left:394px;top:487px;display:flex;gap:4px}
.dots span{width:8px;height:8px;border-radius:50%;background:#bbb}
.dots span.on{background:var(--orange)}

/* cards */
.card{top:535px;width:202px;height:300px;background:var(--card)}
.card-head{height:30px;background:var(--orange);padding:3px 8px;font:700 10.5px/11.5px 'Lato',sans-serif;color:var(--white)}
.card-photo{height:94px}
.card-body{padding:12px 13px 0;font:400 8px/12.3px 'Lato',sans-serif;color:#333}
.card-body p+p{margin-top:12px}
.card-body a{color:var(--teal-dark)}
.more{display:inline-flex;align-items:center;gap:6px;margin-top:8px;height:17px;padding:0 4px 0 6px;background:var(--orange);font:700 8px/1 'Lato',sans-serif;color:var(--white)}
.more i{width:11px;height:11px;border:1px solid #fff;border-radius:50%;display:flex;align-items:center;justify-content:center;font-style:normal;font-size:7px}
.zig{position:absolute;left:0;bottom:-5px}

/* enquiry */
.enquiry{left:0;top:863px;width:832px;height:129px;background:var(--dark)}
.enq-title{left:91px;top:884px;font:400 21px/1 'Lato',sans-serif;color:var(--orange)}
.enq-text{left:91px;top:922px;width:215px;font:400 10.5px/14px 'Lato',sans-serif;color:var(--white)}
.field{background:var(--white);font:400 9px/1 'Lato',sans-serif;color:#555;padding:6px 5px}
.field b{color:var(--orange);font-weight:400}
.submit{left:531px;top:947px;width:64px;height:21px;background:var(--orange);font:700 10px/21px 'Lato',sans-serif;color:var(--white);text-align:center}

/* footer */
.footer{left:0;top:992px;width:832px;height:178px;background:var(--footer)}
.f-title{font:700 11px/1 'Lato',sans-serif;color:var(--orange)}
.f-rule{height:1px;background:#d0d0d0;width:138px;margin-top:8px}
.links{list-style:none;margin-top:4px}
.links li{font:400 8.5px/18.7px 'Lato',sans-serif;color:#333}
.links li::before{content:"›";color:var(--orange);margin-right:8px;font-weight:700}
.f-copy{font:400 8px/11.5px 'Lato',sans-serif;color:#333}
.f-copy p{margin-top:12px}
.f-copy a{color:var(--teal-dark)}
.imp{display:flex;gap:7px;margin-top:12px}
.imp svg{flex:none;margin-top:1px}
.imp h4{font:700 10.5px/1 'Lato',sans-serif;color:#222}
.imp p{font:400 8px/1 'Lato',sans-serif;color:#333;margin-top:5px}
.imp a{color:var(--teal-dark)}

/* bottom */
.social{left:90px;top:1176px;display:flex;gap:4px}
.social span{width:19px;height:19px;border-radius:50%}
.copyright{left:0;top:1181px;width:832px;text-align:center;font:400 8px/1 'Lato',sans-serif;color:#333}
.foot-brand{right:90px;top:1175px;display:flex;align-items:center;gap:5px}
.foot-brand .brand-dot{width:18px;height:18px}
.foot-brand .brand-name{font-size:13px}
</style>
</head>
<body>

<header>
  <div class="abs brand"><span class="brand-dot"></span><span class="brand-name">Tane Drain</span></div>
  <p class="abs header-strap">Our septic tank maintenance services will help your septic system perform at optimum efficiency</p>
  <p class="abs tagline">For Septic Tank servicing, installation and parts<br>Auckland Wide</p>
  <div class="abs phones">
    <svg width="14" height="14" viewBox="0 0 24 24"><path fill="#1aa88a" d="M6.6 10.8a15 15 0 0 0 6.6 6.6l2.2-2.2a1 1 0 0 1 1-.25 11.4 11.4 0 0 0 3.6.57 1 1 0 0 1 1 1V20a1 1 0 0 1-1 1A17 17 0 0 1 3 4a1 1 0 0 1 1-1h3.5a1 1 0 0 1 1 1c0 1.25.2 2.45.57 3.57a1 1 0 0 1-.25 1z"/></svg>
    <span>09 555 0142</span><span class="or">OR</span><span>021 555 07 316</span>
  </div>
</header>

<nav class="abs nav">
  <ul>
    <li class="active">HOME</li><li>ABOUT</li><li>DECIPHERING YOUR SEPTIC TANK</li><li>SERVICING &amp; MAINTENANCE</li><li>PARTS</li><li>FREE QUOTE</li><li>CONTACT</li>
  </ul>
</nav>

<section>
  <div class="abs hero" role="img" aria-label="Photo of waterfalls cascading over a mossy cliff into a green lake"></div>
  <h1 class="abs hero-title">Want to learn more about how your septic tank works?</h1>
  <p class="abs hero-sub">Tane Drain Septic Services are Auckland's best septic tank experts and will tell you everything there is to know...</p>
  <div class="abs hero-btn">
    <svg width="18" height="18" viewBox="0 0 24 24" fill="none" stroke="#fff" stroke-width="2"><rect x="3" y="5" width="14" height="16" rx="1"/><path d="M7 10h6M7 14h4M14 14l7-7 2 2-7 7h-2z"/></svg>
    Quick Contact
  </div>
  <div class="abs dots"><span></span><span class="on"></span><span></span><span></span></div>
</section>

<section>
  <article class="abs card" style="left:89px">
    <h3 class="card-head">Looking for septic tanks parts in Auckland asap?</h3>
    <div class="card-photo" role="img" aria-label="Photo of septic tank treatment product, pumps and replacement parts" style="background:linear-gradient(90deg,#d9d9d4,#b9b6ad 50%,#8d8f8a)"></div>
    <div class="card-body">
      <p>If you need <a href="#">replacement parts for septic tanks,</a> call us today! Tane Drain Septic Services will either have or can source the part you need fast and offer <b>septic tank part installation services</b> to ensure your parts are fitted correctly and work at optimum efficiency for longer. And often we can offer same day service when you're in a bind.</p>
      <span class="more">More Info <i>›</i></span>
    </div>
    <svg class="zig" width="202" height="6"><path d="M0 0 L202 0 L202 1 Q198 6 194 1 Q190 6 186 1 Q182 6 178 1 Q174 6 170 1 Q166 6 162 1 Q158 6 154 1 Q150 6 146 1 Q142 6 138 1 Q134 6 130 1 Q126 6 122 1 Q118 6 114 1 Q110 6 106 1 Q102 6 98 1 Q94 6 90 1 Q86 6 82 1 Q78 6 74 1 Q70 6 66 1 Q62 6 58 1 Q54 6 50 1 Q46 6 42 1 Q38 6 34 1 Q30 6 26 1 Q22 6 18 1 Q14 6 10 1 Q6 6 2 1 L0 1Z" fill="#f4f4f4"/></svg>
  </article>

  <article class="abs card" style="left:315px">
    <h3 class="card-head">Want to know how to take care of your septic tank?</h3>
    <div class="card-photo" role="img" aria-label="Photo of a technician working beside an open septic tank in the ground" style="background:linear-gradient(90deg,#6b5a3e,#4e3f2a 50%,#6f7f4a)"></div>
    <div class="card-body">
      <p>Most people when they buy a new property with a septic tank don't understand how their system works, or even what system they have! Tane Drain Septic Services will come inspect your septic tank anywhere in Auckland and offer DIY maintenance advice to avoid any messy or unnecessary problems with your septic tank.</p>
      <span class="more">More Info <i>›</i></span>
    </div>
    <svg class="zig" width="202" height="6"><path d="M0 0 L202 0 L202 1 Q198 6 194 1 Q190 6 186 1 Q182 6 178 1 Q174 6 170 1 Q166 6 162 1 Q158 6 154 1 Q150 6 146 1 Q142 6 138 1 Q134 6 130 1 Q126 6 122 1 Q118 6 114 1 Q110 6 106 1 Q102 6 98 1 Q94 6 90 1 Q86 6 82 1 Q78 6 74 1 Q70 6 66 1 Q62 6 58 1 Q54 6 50 1 Q46 6 42 1 Q38 6 34 1 Q30 6 26 1 Q22 6 18 1 Q14 6 10 1 Q6 6 2 1 L0 1Z" fill="#f4f4f4"/></svg>
  </article>

  <article class="abs card" style="left:541px">
    <h3 class="card-head">When was the last time you serviced your septic tank?</h3>
    <div class="card-photo" role="img" aria-label="Photo of a suction hose leading to an open septic tank on a lawn" style="background:linear-gradient(180deg,#7d9a4e,#5e7d35 60%,#8a8a6a)"></div>
    <div class="card-body">
      <p>Standard septic tanks need to be serviced every 3 - 5 years and as each septic system has its own unique characteristics, such as internal parts and control panels. It can be difficult to service it thoroughly yourself.</p>
      <p>Tane Drain Septic Services have the experience, supplies and materials to service all septic tank systems, as well as helping you to <a href="#">understand your septic tank system.</a></p>
      <span class="more">More Info <i>›</i></span>
    </div>
    <svg class="zig" width="202" height="6"><path d="M0 0 L202 0 L202 1 Q198 6 194 1 Q190 6 186 1 Q182 6 178 1 Q174 6 170 1 Q166 6 162 1 Q158 6 154 1 Q150 6 146 1 Q142 6 138 1 Q134 6 130 1 Q126 6 122 1 Q118 6 114 1 Q110 6 106 1 Q102 6 98 1 Q94 6 90 1 Q86 6 82 1 Q78 6 74 1 Q70 6 66 1 Q62 6 58 1 Q54 6 50 1 Q46 6 42 1 Q38 6 34 1 Q30 6 26 1 Q22 6 18 1 Q14 6 10 1 Q6 6 2 1 L0 1Z" fill="#f4f4f4"/></svg>
  </article>
</section>

<section>
  <div class="abs enquiry"></div>
  <h2 class="abs enq-title">Make An Enquiry</h2>
  <p class="abs enq-text">Fill out the form below and we will contact you within 24hrs.</p>
  <div class="abs field" style="left:347px;top:887px;width:174px;height:21px"><b>*</b>Name</div>
  <div class="abs field" style="left:347px;top:917px;width:174px;height:21px"><b>*</b>Email</div>
  <div class="abs field" style="left:347px;top:947px;width:174px;height:21px"><b>*</b>Phone</div>
  <div class="abs field" style="left:531px;top:887px;width:212px;height:51px">Detail</div>
  <div class="abs submit">SUBMIT</div>
</section>

<footer>
  <div class="abs footer"></div>
  <div class="abs" style="left:90px;top:1009px">
    <h4 class="f-title">Quick Links</h4><div class="f-rule"></div>
    <ul class="links"><li>Home</li><li>About</li><li>Deciphering Your Septic tank</li><li>Servicing &amp; Maintenance</li><li>Parts</li><li>Free Quote</li><li>Contact</li></ul>
  </div>
  <div class="abs" style="left:270px;top:1009px;width:215px">
    <h4 class="f-title">Company guarantee to you...</h4><div class="f-rule" style="width:215px"></div>
    <div class="f-copy">
      <p style="margin-top:7px">Tane Drain Septic Services travel throughout the Auckland region. Owner Rewi promises they will go through your system with a fine tooth comb and provide a comprehensive service.</p>
      <p>Tane Drain Septic Services aim to give clients more than they expect from their septic tank service.</p>
      <p>And most <a href="#">septic tank parts</a> we sell come with a one year guarantee.</p>
    </div>
  </div>
  <div class="abs" style="left:527px;top:1009px;width:215px">
    <h4 class="f-title">Important Links</h4><div class="f-rule" style="width:215px"></div>
    <div class="imp"><svg width="11" height="11" viewBox="0 0 12 12"><circle cx="6" cy="6" r="5.3" fill="none" stroke="#1aa88a"/><path d="M5 3.5 7.5 6 5 8.5" fill="none" stroke="#1aa88a"/></svg>
      <div><h4>Need your septic tank cleaned?</h4><p>Talk to the team at <a href="#">Kauri Tank Cleaning Services!</a></p></div></div>
    <div class="imp" style="margin-top:22px"><svg width="11" height="11" viewBox="0 0 12 12"><circle cx="6" cy="6" r="5.3" fill="none" stroke="#1aa88a"/><path d="M5 3.5 7.5 6 5 8.5" fill="none" stroke="#1aa88a"/></svg>
      <div><h4>For all polymer fabricated products</h4><p>Talk to the team at Harbourline Plastics Limited</p></div></div>
  </div>

  <div class="abs social" aria-label="Social links">
    <span style="background:#3b5998"></span><span style="background:#2ea7de"></span><span style="background:#1a7bb5"></span><span style="background:#f08a1c"></span>
  </div>
  <p class="abs copyright">© 2014 Tane Drain Septic Services. All rights reserved.</p>
  <div class="abs foot-brand"><span class="brand-dot"></span><span class="brand-name">Tane Drain</span></div>
</footer>

</body>
</html>
```